Business card design, sleek & clean . For a notary loan signing business. I work with several lenders escrow officers etc . I am bilingual in Spanish , work 7 days a week to meet clients needs. Loan documents can be emailed for printing.

Not sure sleek clean logo

```html
<!DOCTYPE html>
<html lang="en">
<head>
<meta charset="utf-8">
<title>Marisol Ventura – Notary Public Business Card</title>
<link href="https://fonts.googleapis.com/css2?family=Cinzel:wght@400&family=Noto+Sans+JP:wght@400;500&display=swap" rel="stylesheet">
<style>
  :root {
    --navy: #1c3a6a;
    --gold: #d8a52a;
    --white: #ffffff;
    --card-light: #eef6f9;
    --page: #ffffff;
  }
  * { margin: 0; padding: 0; box-sizing: border-box; }
  html, body { width: 1097px; height: 1200px; overflow: hidden; background: var(--page); }
  .canvas { position: relative; width: 1097px; height: 1200px; }

  .card { position: absolute; left: 148px; width: 807px; height: 486px; }
  .card--front { top: 84px; background: var(--navy); }
  .card--back { top: 624px; background: var(--card-light); }

  .brand-name {
    position: absolute;
    font-family: "Cinzel", "Times New Roman", serif;
    font-weight: 400;
    color: var(--gold);
    white-space: nowrap;
  }
  .card--front .brand-name {
    left: 0; right: 0; top: 202px; text-align: center;
    font-size: 44px; letter-spacing: 2px;
  }
  .tagline {
    position: absolute; left: 0; right: 0; top: 300px; text-align: center;
    font-family: "Noto Sans JP", Arial, sans-serif;
    font-size: 20px; letter-spacing: 12px; color: var(--white);
    padding-left: 12px;
  }

  .card--back .brand-name {
    left: 46px; width: 337px; top: 258px; text-align: center;
    font-size: 28px; letter-spacing: 1px;
  }
  .divider {
    position: absolute; left: 403px; top: 91px; width: 1px; height: 301px;
    background: var(--navy);
  }
  .contact-list { position: absolute; left: 420px; top: 160px; list-style: none; }
  .contact-item {
    display: flex; align-items: center; height: 44px;
    font-family: "Noto Sans JP", Arial, sans-serif;
    font-size: 22px; color: var(--navy); white-space: nowrap;
  }
  .contact-item svg { width: 30px; height: 30px; margin-right: 11px; flex: none; }
  .availability {
    position: absolute; left: 0; width: 807px; top: 440px; text-align: center;
    font-family: "Noto Sans JP", Arial, sans-serif;
    font-size: 19px; font-weight: 500; color: var(--navy);
  }
  .chat-mark { position: absolute; left: 758px; top: 439px; width: 30px; height: 30px; }
</style>
</head>
<body>
<div class="canvas">

  <section class="card card--front">
    <h1 class="brand-name">MARISOL VENTURA</h1>
    <p class="tagline">NOTARY PUBLIC</p>
  </section>

  <section class="card card--back">
    <p class="brand-name">MARISOL VENTURA</p>
    <div class="divider"></div>
    <ul class="contact-list">
      <li class="contact-item">
        <svg viewBox="0 0 30 30" aria-hidden="true"><path d="M7 3c2 0 3 4 4 6s-2 3-1 5 3 4 5 5 3-2 5-1 6 2 6 4-3 5-6 5C15 27 3 15 3 8c0-3 2-5 4-5z" fill="var(--gold)"/></svg>
        (555)014-2398
      </li>
      <li class="contact-item">
        <svg viewBox="0 0 30 30" aria-hidden="true"><rect x="2" y="6" width="26" height="19" rx="1" fill="var(--gold)"/><path d="M3 7l12 10 12-10" fill="none" stroke="var(--card-light)" stroke-width="2"/></svg>
        mventura_ca@example.com
      </li>
      <li class="contact-item">
        <svg viewBox="0 0 30 30" aria-hidden="true"><circle cx="15" cy="16" r="11" fill="none" stroke="var(--gold)" stroke-width="2.5"/><path d="M9 15l5 5 11-13" fill="none" stroke="var(--gold)" stroke-width="2.5" stroke-linecap="round"/></svg>
        Habb Espanol
      </li>
      <li class="contact-item">
        <svg viewBox="0 0 30 30" aria-hidden="true"><circle cx="15" cy="16" r="11" fill="none" stroke="var(--gold)" stroke-width="2.5"/><path d="M9 15l5 5 11-13" fill="none" stroke="var(--gold)" stroke-width="2.5" stroke-linecap="round"/></svg>
        Loan Packaging ; Printing
      </li>
    </ul>
    <p class="availability">7 DAYS A WEEK TO MEET CLIENTS NEEDS</p>
    <svg class="chat-mark" viewBox="0 0 30 30" aria-hidden="true"><circle cx="15" cy="15" r="12" fill="none" stroke="var(--gold)" stroke-width="2.5"/></svg>
  </section>

</div>
</body>
</html>
```